Premium Gold Vodka Label Design

English ------------------- We need a label for a Vodka Bottle. Its a sparkling premium vodka with gold inside. The design should look premium. We tried it on our selves but it looks horrible. Therefore we need your help. The current name is corvelle K, but we are open for any better suggestion. We attached the selfmade design. The label will be printed on the bottle. We have other design jobs for you (logo, other sorts)! English ------------------------ We need a label for a vodka bottle. This is a premium vodka which is offset with gold. The design should look like this. We have tried so far and failed. That is why we need your support. The name is so far corvelle K. If you have better suggestions we would be pleased about other suggestions / ideas. In the appendix the failed design is stored. The label is to be applied by screen printing. In the case of good work follow-up projects are guaranteed (logo, other varieties, etc)!
Updates

Reason: We need more time for the decision.

Target Market(s)

USA

Colors

Designer to choose colors to be used in the design.

Requirements
Must have
• English ------------------------ The needed text is on our selfmade label that is attached. English ------------------------ The required texts are stored in the attached design.
Nice to have
• English ------------------------ Transparent places are allowed because we want to print the label on the bottom. English ------------------------ As the label is applied by screen printing, transparent areas are also possible.

```html
<!DOCTYPE html>
<html lang="en">
<head>
<meta charset="utf-8">
<title>corvelle K Premium Gold Sparkling Vodka – Labels</title>
<link rel="stylesheet" href="https://fonts.googleapis.com/css2?family=Orbitron:wght@500;700&family=Audiowide&display=swap">
<style>
  :root {
    --bg-deep: #050505;
    --bg-soft: #1c1d1f;
    --gold: #c9a02e;
    --gold-light: #e6c45a;
    --gold-dark: #8f6c14;
    --ink: #111111;
    --ink-soft: #2a2a2a;
  }
  * { margin: 0; padding: 0; box-sizing: border-box; }
  html, body { width: 1140px; height: 1200px; overflow: hidden; }
  body {
    background: radial-gradient(ellipse at 50% 45%, var(--bg-soft) 0%, var(--bg-deep) 70%);
    font-family: "Orbitron", sans-serif;
    position: relative;
  }
  .label {
    position: absolute;
    top: 290px;
    width: 460px;
    height: 620px;
    padding: 14px;
  }
  .label--gold { left: 80px; background: linear-gradient(135deg, var(--gold-dark), var(--gold) 35%, var(--gold-light) 60%, var(--gold) 100%); }
  .label--black { left: 600px; background: var(--ink); }
  .label__frame {
    position: relative;
    width: 100%;
    height: 100%;
    border: 4px solid var(--ink);
    display: flex;
    flex-direction: column;
    align-items: center;
  }
  .label--black .label__frame { border-color: var(--gold); }
  .brand-name {
    margin-top: 92px;
    font-family: "Orbitron", sans-serif;
    font-weight: 700;
    font-size: 50px;
    letter-spacing: 1px;
    color: var(--ink);
  }
  .label--black .brand-name { color: var(--gold); }
  .grade-band {
    margin-top: 84px;
    width: 100%;
    height: 86px;
    background: var(--ink);
    display: flex;
    flex-direction: column;
    align-items: center;
    justify-content: center;
    position: relative;
  }
  .label--black .grade-band {
    background: linear-gradient(90deg, var(--gold-dark), var(--gold-light) 50%, var(--gold-dark));
  }
  .grade-band__title {
    font-family: "Audiowide", sans-serif;
    font-size: 34px;
    color: var(--gold);
    line-height: 1;
  }
  .grade-band__sub {
    font-weight: 500;
    font-size: 18px;
    letter-spacing: 8px;
    color: var(--gold);
    margin-top: 6px;
  }
  .label--black .grade-band__title,
  .label--black .grade-band__sub { color: var(--ink); }
  .karat-tab {
    width: 90px;
    height: 34px;
    background: var(--ink);
    border-radius: 0 0 45px 45px;
    color: var(--gold);
    font-family: "Audiowide", sans-serif;
    font-size: 18px;
    text-align: center;
    line-height: 28px;
  }
  .product {
    margin-top: 24px;
    font-weight: 700;
    font-size: 52px;
    letter-spacing: 22px;
    padding-left: 22px;
    color: var(--ink);
  }
  .label--black .product { color: var(--gold); }
  .process, .origin {
    font-weight: 500;
    color: var(--ink);
  }
  .process { margin-top: 10px; font-size: 14px; letter-spacing: 4px; }
  .origin { margin-top: 10px; font-size: 12px; letter-spacing: 1px; }
  .label--black .process, .label--black .origin { color: var(--gold-light); }
  .specs {
    position: absolute;
    bottom: 18px;
    left: 50px;
    right: 50px;
    display: flex;
    justify-content: space-between;
    font-weight: 500;
    font-size: 11px;
    color: var(--ink);
  }
  .label--black .specs { color: var(--gold-light); }
</style>
</head>
<body>
  <section class="label label--gold" aria-label="Gold label variant">
    <div class="label__frame">
      <div class="brand-name">corvelle K</div>
      <div class="grade-band">
        <span class="grade-band__title">PREMIUM GOLD</span>
        <span class="grade-band__sub">SPARKLING</span>
      </div>
      <div class="karat-tab">24kt</div>
      <div class="product">VODKA</div>
      <div class="process">Distilled and Filtered</div>
      <div class="origin">Made in Germany</div>
      <div class="specs"><span>40 Alc Vol</span><span>200ml</span><span>80Proof</span></div>
    </div>
  </section>

  <section class="label label--black" aria-label="Black label variant">
    <div class="label__frame">
      <div class="brand-name">corvelle K</div>
      <div class="grade-band">
        <span class="grade-band__title">PREMIUM GOLD</span>
        <span class="grade-band__sub">SPARKLING</span>
      </div>
      <div class="karat-tab">24kt</div>
      <div class="product">VODKA</div>
      <div class="process">Distilled and Filtered</div>
      <div class="origin">Made in Germany</div>
      <div class="specs"><span>40 Alc Vol</span><span>200ml</span><span>80Proof</span></div>
    </div>
  </section>
</body>
</html>
```